Packaging design for children’s shampoo bar

A design that could be used on solid shampoo and soap wraps then amended for jar labels. The packaging needs to be bright and child-friendly. We have a logo and a pattern, but please feel free to change them. I think it needs to be brighter.

I would like each product to have an accent colour and for the shampoo I am thinking of blue/teal. This will be complemented by the body wash bar (pink) and toothpaste (orange).

The shampoo bar wrap needs to contain the following information:

Pippin & Pals logo
Shampoo Bar
100% natural
Vegan & Palm Oil-Free
Weight 85 g
Made in the U.K.

Ingredients: sodium hydroxide, prunus amygdalus dulcis oil, olea europaea oil, cocos nucifera oil, ricinus communis seed oil, simmondsia chinensia seed oil.

Contact details: Pippin & Pals, Marlow Tessing House, London N7 4QB. Website: www.Pippin and pals.co.U.K.

Brand board is here: https://www.filecrate.example/s/k8rw2mzatqvexbd/Photo%2003-07-2020%2C%2021%2040%2034.jpg?dl=0

Inspiration is here: https://kitebirdstudio.example/collections/beauty-grooming/products/dog-shampoo-100-natural-vegan

These are the wraps we shall be using: https://www.nearbypressworks.example/soap-wrap

Thank you so much for your interest in this project!

Target Market(s)

Children 5-12 years.

Requirements
Must have
• Clean design. Lots of white with bright colours.

```html
<!DOCTYPE html>
<html lang="en">
<head>
<meta charset="utf-8">
<title>Pippin &amp; Pals — Shampoo Bar Wrap</title>
<link rel="stylesheet" href="https://fonts.googleapis.com/css2?family=Amatic+SC:wght@700&family=Montserrat:wght@600&family=Jost:wght@400;600&family=EB+Garamond:wght@500&display=swap">
<style>
  :root {
    --bg: #e6e7e8;
    --wrap: #ffffff;
    --wrap-edge: #f1f1f2;
    --shampoo-blue: #9fd2e5;
    --leaf-green: #8aab4a;
    --coral: #e88f6a;
    --grey-text: #7d7d7f;
    --ink: #1d1d1f;
    --faint: #e2e3e5;
    --pill: #8e8e90;
  }
  * { box-sizing: border-box; margin: 0; padding: 0; }
  html, body { width: 1200px; height: 839px; overflow: hidden; }
  body { background: var(--bg); font-family: "Jost", sans-serif; color: var(--ink); }

  .canvas { position: relative; width: 1200px; height: 839px; }

  .wrap-panel {
    position: absolute;
    left: 60px;
    width: 1080px;
    height: 380px;
    background: linear-gradient(180deg, var(--wrap) 0%, var(--wrap-edge) 100%);
    border-radius: 14px;
    box-shadow: 0 6px 18px rgba(0,0,0,0.10);
    overflow: hidden;
  }
  .wrap-front { top: 28px; }
  .wrap-back { top: 432px; }

  /* Front */
  .brand-mark {
    position: absolute;
    left: 70px; top: 150px;
    display: flex; align-items: center; gap: 12px;
  }
  .brand-dot { width: 22px; height: 22px; border-radius: 50%; background: var(--shampoo-blue); }
  .brand-name {
    font-family: "Amatic SC", sans-serif;
    font-weight: 700;
    font-size: 58px;
    color: var(--coral);
    line-height: 1;
  }
  .front-copy {
    position: absolute;
    left: 430px; right: 40px; top: 100px;
    text-align: center;
  }
  .claim {
    font-family: "Montserrat", sans-serif;
    font-weight: 600;
    color: var(--grey-text);
    letter-spacing: 0.5px;
  }
  .front-copy .claim { font-size: 22px; }
  .product-name {
    font-family: "Amatic SC", sans-serif;
    font-weight: 700;
    color: var(--shampoo-blue);
    line-height: 0.95;
  }
  .front-copy .product-name { font-size: 96px; margin-top: 2px; }
  .tagline-front {
    font-family: "Amatic SC", sans-serif;
    font-weight: 700;
    font-size: 38px;
    color: var(--leaf-green);
    margin-top: 6px;
  }
  .weight-front {
    font-size: 13px;
    letter-spacing: 0.5px;
    margin-top: 34px;
  }

  /* Back */
  .back-copy { position: absolute; left: 60px; top: 52px; width: 260px; }
  .back-copy .claim { font-size: 15px; }
  .back-copy .product-name { font-size: 52px; margin-top: 2px; }
  .tagline-back {
    font-family: "EB Garamond", serif;
    font-weight: 500;
    font-size: 15px;
    color: var(--leaf-green);
    margin-top: 2px;
  }
  .ingredients {
    font-size: 12.5px;
    line-height: 1.35;
    width: 250px;
    margin-top: 26px;
  }
  .ingredients strong, .contact-name { font-weight: 600; }
  .contact { font-size: 12.5px; line-height: 1.4; margin-top: 20px; width: 260px; }
  .origin { font-size: 7.5px; font-weight: 600; letter-spacing: 0.4px; margin-top: 10px; }

  .brand-faint {
    position: absolute;
    right: 170px; top: 118px;
    font-family: "Amatic SC", sans-serif;
    font-weight: 700;
    font-size: 78px;
    color: var(--faint);
    line-height: 1;
  }
  .weight-pill {
    position: absolute;
    right: 130px; bottom: 44px;
    background: var(--pill);
    color: #fff;
    font-size: 11px;
    padding: 3px 10px;
    border-radius: 10px;
    letter-spacing: 0.3px;
  }
</style>
</head>
<body>
<main class="canvas">
  <section class="wrap-panel wrap-front" aria-label="Shampoo bar wrap, front">
    <div class="brand-mark">
      <span class="brand-dot"></span>
      <span class="brand-name">Pippin &amp; Pals</span>
    </div>
    <div class="front-copy">
      <p class="claim">100% NATURAL</p>
      <h1 class="product-name">SHAMPOO BAR</h1>
      <p class="tagline-front">Vegan &amp; Palm Oil-Free</p>
      <p class="weight-front">–&nbsp; WEIGHT 85 G &nbsp;–</p>
    </div>
  </section>

  <section class="wrap-panel wrap-back" aria-label="Shampoo bar wrap, back">
    <div class="back-copy">
      <p class="claim">100% NATURAL</p>
      <h2 class="product-name">SHAMPOO BAR</h2>
      <p class="tagline-back">Vegan &amp; Palm Oil-Free</p>
      <p class="ingredients"><strong>Ingredients:</strong> Sodium hydroxide, prunus amygdalus dulcis oil, olea europaea oil, cocos nucifera oil, ricinus communis seed oil, simmondsia chinensia seed oil.</p>
      <p class="contact"><span class="contact-name">Pippin &amp; Pals</span><br>Marlow Tessing House, London N7 4QB.<br>Website: www.Pippin and pals.co.U.K.</p>
      <p class="origin">MADE IN THE U.K.</p>
    </div>
    <span class="brand-faint">Pippin &amp; Pals</span>
    <span class="weight-pill">WEIGHT 85 G</span>
  </section>
</main>
</body>
</html>
```